Brochure for Community-Based Therapy Company

Will be given out to patients, doctors, case managers. We are redesigning our marketing materials and would like a design for a brochure. We provide therapy to individuals who have been injured in car accidents or on the job. We provide occupational therapy, speech therapy and psychotherapy. We would like the brochure to utilize our corporate ID and color scheme that we are using for our other materials (see attached letterhead and logo).

Stock photos that are used should stay away from images of outpatient or hospital settings, stay away from photos with obvious disabilities (wheelchairs, learning to walk, etc), and nothing that looks like physical therapy, as we don't provide physical therapy only OT, Speech and psychotherapy. Would prefer to not have people wearing masks, as we will use this beyond the pandemic. Also, our staff wears business casual clothing so would prefer photos that the individuals are not wearing scrubs or other medical attire (lab coats, etc).

Target Market(s)

Patients, Physicians/Doctors, Case Managers

Industry/Entity Type

Healthcare

Requirements
Must have
• Prefer a booklet format but doesn't have to be 8.5 inch by 11 inch (can be a little smaller).

```html
<!DOCTYPE html>
<html lang="en">
<head>
<meta charset="utf-8">
<title>Services Offered</title>
<link href="https://fonts.googleapis.com/css2?family=Jost:wght@400;500&family=Oswald:wght@300&display=swap" rel="stylesheet">
<style>
  :root {
    --paper: #ffffff;
    --ink: #1a1a1a;
    --muted: #8a8a8a;
    --heading: #6f6f6f;
    --accent: #8fb1a8;
  }
  html, body { margin: 0; padding: 0; overflow: hidden; background: var(--paper); }
  .spread {
    position: relative;
    width: 1200px; height: 776px;
    overflow: hidden;
    background: var(--paper);
    font-family: "Jost", sans-serif;
    color: var(--ink);
  }
  .page-title {
    position: absolute; left: 0; width: 908px; top: 50px; margin: 0;
    text-align: center; font-weight: 400; font-size: 19px; letter-spacing: 0.02em;
  }
  .section-heading {
    position: absolute; margin: 0;
    font-family: "Oswald", sans-serif; font-weight: 300;
    font-size: 13px; letter-spacing: 0.12em; color: var(--heading);
  }
  .intro {
    position: absolute; margin: 0;
    font-size: 9.6px; line-height: 11.6px;
  }
  .includes-label {
    position: absolute; margin: 0;
    font-size: 9.5px; letter-spacing: 1.05em; font-weight: 400;
  }
  .service-list {
    position: absolute; margin: 0;
    font-size: 9.8px; line-height: 15.6px;
  }
  .service-list.tight { line-height: 13.8px; }
  .service-list .hi { color: var(--ink); }
  .service-list .lo { color: var(--muted); }
  .sep { color: var(--accent); font-weight: 500; padding: 0 2px; }
  .plain-line {
    position: absolute; margin: 0; font-size: 9.8px; line-height: 15.6px;
  }
</style>
</head>
<body>
<main class="spread">
  <h1 class="page-title">SERVICES OFFERED</h1>

  <!-- Speech language pathology -->
  <h2 class="section-heading" style="left:88px; top:90px;">SPEECH LANGUAGE PATHOLOGY</h2>
  <p class="intro" style="left:88px; top:114px; width:444px;">Speech &amp; Language Pathologists are trained in the rehabilitation of deficits/disorders in the areas of language, articulation, voice, fluency, and dysphagia, with an underlying knowledge base of the neurological and physiologic processes affecting each. Deficits in the areas of attention, memory, information processing and executive functioning can impact all of the areas that speech and language pathologists treat, and are addressed in all treatment goals.</p>
  <h3 class="includes-label" style="left:139px; top:196px;">SERVICES INCLUDE:</h3>
  <p class="service-list" style="left:139px; top:216px; width:368px;">
    <span class="hi">Immediate and Short-Term Memory: compensatory strategies, modification of the environment for increased functional memory</span><span class="sep">|</span><span class="lo">Attention and concentration</span><span class="sep">|</span>
    <span class="hi">Expressive Language: ability to express ideas, verbally, or in written format, in a concise organized fashion</span><span class="sep">|</span><span class="lo">Comprehension and Retention of Verbal and Written Language</span><span class="sep">|</span><span class="hi">Information Processing: gradually increase in the length and complexity of information presented to allow the brain to take in and process more information at one time</span><span class="sep">|</span><span class="lo">Word Retrieval and Thought Formulation for Verbal and Written Expression</span><span class="sep">|</span><span class="hi">Pragmatic Language/Social Communication</span><span class="sep">|</span>
    <span class="lo">Executive Functioning: The mental processes that enable individuals toplan, focus attention, retain instructions, and juggle multiple tasks successfully. Assist with planning, initiating, carrying out tasks, as well as assist with self-monitoring and awareness for carryover of strategies</span><span class="sep">|</span><span class="hi">Articulation</span><span class="sep">|</span><span class="lo">Dysarthria (lack of voluntary control)</span><span class="sep">|</span><span class="hi">Dysphagia (swallowing disorders)</span><span class="sep">|</span><span class="lo">Voice</span>
  </p>

  <!-- Occupational therapy -->
  <h2 class="section-heading" style="left:88px; top:459px;">OCCUPATIONAL THERAPY</h2>
  <p class="intro" style="left:88px; top:489px; width:444px;">Occupational Therapists are experts at the evaluation and analysis of an individual’s abilities relative to the demands of an activity and use this perspective in order to determine any aspects of the person’s life that have been impacted, including activities of daily living (i.e., self-care), instrumental activities of daily living (i.e., home management, rest and sleep habits, work demands, play, leisure, and social participation). Treatment includes re-learning how to do activities (remediation) or determining new ways of accomplishing them (compensatory strategies).</p>
  <h3 class="includes-label" style="left:139px; top:581px;">SERVICES INCLUDE:</h3>
  <p class="service-list tight" style="left:139px; top:601px; width:368px;">
    <span class="lo">Treatment of musculoskeletal (i.e., muscle strength, range of motion), sensory, perceptual, vestibular, and vascular, skin, or connective tissue impairments</span><span class="sep">|</span>
    <span class="hi">Teach the use of memory compensation techniques such as daily planners, technological devices, checklists, and cueing systems</span><span class="sep">|</span><span class="lo">Assist in developing effective schedules and routines</span><span class="sep">|</span><span class="lo">Instruct individuals and family members in techniques to cope with behavioral changes and low frustration tolerance</span><span class="sep">|</span><span class="hi">Assessment and treatment to maximize safety in the home and community environments</span><span class="sep">|</span>
  </p>

  <!-- Right page: OT continued -->
  <p class="service-list" style="left:738px; top:67px; width:374px;">
    <span class="lo">Recommendation of environmental adaptations to assist with physical, perceptual, and cognitive functioning, such as labeling cupboards and drawers, or using lighting to improve vision and/or attention to task</span><span class="sep">|</span><span class="hi">Assist in re-learning social skills through techniques such as pre-processing and rehearsal, where the individual and therapist anticipate challenging social situations and practice appropriate responses</span><span class="sep">|</span><span class="lo">Provide cognitive retraining exercises to address specific cognitive skills, such as attention, memory, and executive functioning</span><span class="sep">|</span><span class="hi">Provide training and adaptation for activities of daily living, such as dressing, bathing, and grooming</span><span class="sep">|</span><span class="lo">Provide training and assist in the development of compensatory techniques for instrumental activities of daily living, such as preparing meals, shopping, managing routine financial tasks, and caring for children</span><span class="sep">|</span><span class="hi">Assist individuals with community re-integration, working with individuals in real life settings such as the grocery store, bank, mall, workplace, home, or any other environment in which individuals need to regain competence in occupational performance.</span><span class="sep">|</span><span class="lo">Facilitate the identification and development of healthy, meaningful hobbies or other leisure activities</span><span class="sep">|</span>
    <span class="hi">Consult with employers and/or educational systems to adapt the work or school environment to facilitate the individual’s performance abilities</span>
  </p>

  <!-- Psychological -->
  <h2 class="section-heading" style="left:680px; top:358px;">PSYCHOLOGICAL AND COUNSELING</h2>
  <p class="plain-line" style="left:736px; top:388px;">Individual &amp; Family Counseling related to the injury</p>
  <p class="plain-line" style="left:736px; top:411px;">Psychological services are provided as needed and prescribed by the physician to:</p>
  <p class="service-list" style="left:736px; top:431px; width:376px;">
    <span class="lo">Address psychosocial needs of the patient.</span><span class="sep">|</span><span class="hi">Address changes in family dynamics and other changes.</span><span class="sep">|</span><span class="lo">Counsel the patient to ease symptoms of depression.</span><span class="sep">|</span><span class="lo">Assist with acceptance of change of life status, as a result of the injury.</span><span class="sep">|</span><span class="hi">Provide the individual with coping strategies.</span>
  </p>

  <!-- Vocational -->
  <h2 class="section-heading" style="left:684px; top:519px;">VOCATIONAL SERVICES</h2>
  <p class="intro" style="left:686px; top:546px; width:420px;">As traditional cognitive therapy progresses and the patient is making strong progress in the areas of safety, memory, organization and other challenges, the next step is prevocational skill development or work toward a return to school or other training programs. Our occupational therapists work with patients on the following areas in order to work toward a return to work, school or training program which can include the following:</p>
  <p class="service-list" style="left:736px; top:618px; width:376px;">
    <span class="lo">Vocational Assessment, which includes standardized testing in order to determine the patient’s aptitudes and interests in order to determine the most appropriate vocational goal/plan for the patient to be successful</span><span class="sep">|</span><span class="hi">Vocational exploration, job development, educational options and exploration, volunteer exploration</span><span class="sep">|</span>
    <span class="hi">Academic support and tutoring</span><span class="sep">|</span><span class="lo">Job analysis, job site evaluation, job coaching, job placement and shadowin</span><span class="sep">|</span><span class="hi">Coordination with employers or school personnel to ensure adequate accommodations are in place</span>
  </p>
</main>
</body>
</html>
```